Brellin Trade Partners - we are Asian sourcing agents

We are sourcing agents based in the USA and we act as sourcing agents for clients in throughout the world. We focus primarily on custom sewn goods. So basically companies who do not have the in-house expertise to do it themselves, come to us and have us find suitable factories in Asia to do the production. We are middlemen. We find the factories...quote the project...manage the quality control and then deliver the goods directly to our customer's door. We pride ourselves in making the communication very easy and precise.

Current page is www.brellintrade.example

I am not happy w/ the overall look. The spacing...the photos, the fonts...the design elements...the pictures. I want a cool, crisp design that conveys professionalism and clearly depicts/explains what we do.

Requirements
Must have
• use my logo....I like it...it was designed by someone on this website.
Nice to have
• a video/animation of the entire process would be wonderful. Showing initial contact with our office in the USA...then to my correspondence with my offices in Taiwan and in Hong Kong...and then back and fort w/ the customer.....and then between my people in Hong Kong/Taiwan with the local factories......and then a quote is generated and sent to my client......to samples being made and sent for approval.....to a PO being generated......to final samples being sent.....to the order being shipped and delivered to the clients warehouse. I was thinking of an animation showing arrows and text showing the back and forth communication and explaining how the process flows.

```html
<!DOCTYPE html>
<html lang="en">
<head>
<meta charset="utf-8">
<title>Brellin Trade Partners – Asia Sourcing Agents</title>
<link href="https://fonts.googleapis.com/css2?family=PT+Sans:wght@400;700&family=Roboto+Slab:wght@400;700&display=swap" rel="stylesheet">
<style>
:root{
  --green:#76921a;
  --navy:#0f1d5c;
  --ink:#2b2b2b;
  --text:#3c3c3c;
  --muted:#8a8a8a;
  --line:#cfcfcf;
  --panel:#f0f0f0;
  --topbar:#ececec;
  --dark:#2f2f2f;
  --footer:#333333;
  --footer-deep:#161616;
  --white:#ffffff;
}
*{box-sizing:border-box;margin:0;padding:0}
html,body{width:1200px;height:2632px;overflow:hidden}
body{position:relative;background:var(--white);font-family:"PT Sans",Arial,sans-serif;color:var(--text)}
.abs{position:absolute}

/* top strip */
.topbar{left:0;top:0;width:1200px;height:40px;background:var(--topbar)}
.topbar-edge{left:1100px;top:0;width:100px;height:40px;background:var(--dark)}
.social{left:114px;top:8px;display:flex;gap:6px}
.social span{width:24px;height:24px;border:1.5px solid #b5b5b5;border-radius:50%;background:#fafafa}
.shipping{left:294px;top:12px;font:12px "Roboto Slab",serif;color:#555}
.contact{left:826px;top:12px;font:12px "Roboto Slab",serif;color:#555;display:flex;gap:16px;align-items:center}

/* side bands */
.band-green{left:0;top:40px;width:100px;height:197px;background:var(--green)}
.band-navy{left:1100px;top:40px;width:100px;height:197px;background:var(--navy)}

/* header */
.header{left:100px;top:40px;width:1000px;height:197px;background:var(--white)}
.brand{left:118px;top:84px;display:flex;align-items:center;gap:12px}
.brand-mark{width:66px;height:66px;border-radius:50%;background:var(--navy)}
.brand-name{font:700 25px/1.05 "PT Sans",sans-serif;color:var(--navy);width:220px}
.search{left:596px;top:80px;display:flex;align-items:center;gap:8px}
.search-btn{width:36px;height:36px;border-radius:50%;background:#c9c9c9;display:flex;align-items:center;justify-content:center}
.search-field{width:160px;height:36px;border:1px solid #dcdcdc;font:11px "Roboto Slab",serif;color:#999;padding:11px 8px}
.expert{left:822px;top:86px;display:flex;align-items:center;gap:10px;font:12px "Roboto Slab",serif;color:#555}
.expert-dot{width:26px;height:26px;border-radius:50%;background:#f2b600}
.expert a{color:#3a7bc8;text-decoration:underline}
.nav{left:504px;top:149px;display:flex;gap:22px}
.nav span{background:#f2f2f2;padding:10px 14px;font:12px "Roboto Slab",serif;color:#333;letter-spacing:.5px}

/* call bar */
.callbar{left:0;top:237px;width:598px;height:79px;background:var(--green);display:flex;align-items:center;padding-left:154px;gap:12px;color:var(--white);font:20px "PT Sans",sans-serif}
.promo{left:598px;top:237px;width:602px;height:79px;background:var(--navy);display:flex;align-items:center;padding-left:48px;gap:14px;color:var(--white);font:20px "PT Sans",sans-serif}
.ico-round{width:32px;height:32px;border-radius:50%;background:rgba(255,255,255,.18);display:flex;align-items:center;justify-content:center}

/* hero */
.hero{left:0;top:316px;width:1200px;height:497px;background:linear-gradient(100deg,#8f9aa6 0%,#6f7a86 45%,#4f5966 100%);border-bottom:2px solid var(--green)}
.hero-kicker{left:0;top:508px;width:1200px;text-align:center;color:#eef1f4;font:20px "PT Sans",sans-serif}
.hero-title{left:0;top:538px;width:1200px;text-align:center;color:var(--white);font:50px/58px "PT Sans",sans-serif}
.hero-btn{left:535px;top:714px;width:154px;height:50px;border:1px solid rgba(255,255,255,.85);color:var(--white);font:20px/48px "PT Sans",sans-serif;text-align:center}

/* section titles */
.sec-title{left:0;width:1200px;text-align:center;font:38px "PT Sans",sans-serif;color:var(--navy)}
.sec-title em{font-style:normal;color:var(--green)}
.rule{height:2px;background:var(--line)}
.rule i{position:absolute;left:50%;top:-1px;width:64px;height:4px;margin-left:-32px;background:var(--green)}
.copy{text-align:center;font:16.5px/26px "PT Sans",sans-serif;color:var(--text)}

/* product cards */
.card{width:263px;height:266px;background:var(--white);box-shadow:0 1px 6px rgba(0,0,0,.22)}
.card-head{height:49px;color:var(--white);font:23px/49px "PT Sans",sans-serif;text-align:center}
.card-head.navy{background:var(--navy)}
.card-head.green{background:var(--green)}
.card-body{position:absolute;left:14px;top:63px;width:235px;height:189px;background:var(--panel)}
.card-photo{position:absolute;left:38px;top:14px;width:159px;height:110px;border-radius:4px}
.card-label{position:absolute;left:14px;top:140px;width:207px;height:40px;background:var(--white);text-align:center;font:17px/40px "PT Sans",sans-serif;color:#444}
.divider{left:167px;top:1508px;width:859px;border-top:1px dashed #d4d4d4}

/* footer */
.footer{left:0;top:2217px;width:1200px;height:358px;background:var(--footer)}
.footbar{left:0;top:2575px;width:1200px;height:57px;background:var(--footer-deep);color:#e8e8e8;font:14px/57px "PT Sans",sans-serif;text-align:center}
.f-head{font:700 12px "Roboto Slab",serif;color:var(--white);letter-spacing:.3px;text-transform:uppercase}
.f-row{display:flex;gap:16px;align-items:flex-start;color:#e6e6e6;font:12px/18px "Roboto Slab",serif}
.f-ico{flex:none;width:40px;height:40px;border-radius:50%;background:var(--navy);display:flex;align-items:center;justify-content:center}
.tags{display:flex;flex-wrap:wrap;gap:7px;width:240px}
.tags span{border:1px solid #777;padding:5px 6px;font:700 10px "Roboto Slab",serif;color:var(--white);letter-spacing:.3px}
.stores{width:206px}
.stores div{display:flex;justify-content:space-between;border-bottom:1px solid #444;padding:9px 0 10px;font:700 12px "Roboto Slab",serif;color:var(--white)}
.stores div b{color:#888;font-weight:400}
.fb{width:212px}
.fb-top{display:flex;gap:8px;align-items:center;color:var(--white);font:700 11px "Roboto Slab",serif}
.fb-mark{width:36px;height:36px;background:#555}
.fb-follow{display:inline-block;margin-top:3px;width:38px;height:14px;background:#4a66a0}
.fb-count{margin-top:12px;border-top:1px solid #666;padding-top:6px;font:9px "Roboto Slab",serif;color:#bbb}
.fb-grid{margin-top:6px;display:grid;grid-template-columns:repeat(4,40px);gap:6px}
.fb-grid span{width:40px;height:40px;background:linear-gradient(135deg,#8c8070,#5d6470)}
.fb-foot{margin-top:8px;border-top:1px solid #666;padding-top:4px;font:9px "Roboto Slab",serif;color:#ccc}
</style>
</head>
<body>

<div class="abs topbar"></div>
<div class="abs topbar-edge"></div>
<div class="abs social" aria-label="Social links"><span></span><span></span><span></span><span></span><span></span></div>
<div class="abs shipping">Free Shipping orders over $100</div>
<div class="abs contact"><span>✉ hello@brellintrade.example</span><span>☏ +1 555 014 2880</span></div>

<div class="abs band-green"></div>
<div class="abs band-navy"></div>

<header class="abs header"></header>
<div class="abs brand">
  <span class="brand-mark"></span>
  <span class="brand-name">Brellin Trade Partners</span>
</div>
<div class="abs search">
  <span class="search-btn"><svg width="16" height="16" viewBox="0 0 16 16"><circle cx="6.5" cy="6.5" r="4.5" fill="none" stroke="#fff" stroke-width="2"/><line x1="10" y1="10" x2="14" y2="14" stroke="#fff" stroke-width="2.4" stroke-linecap="round"/></svg></span>
  <span class="search-field">Search Site</span>
</div>
<div class="abs expert"><span class="expert-dot"></span><span>Expert In Yacht Industry <a>Since 1949</a></span></div>
<nav class="abs nav"><span>HOME</span><span>SHOP</span><span>PAGES</span><span>FEATURES</span><span>PORTFOLIO</span><span>ELEMENTS</span></nav>

<div class="abs callbar">
  <span class="ico-round"><svg width="16" height="16" viewBox="0 0 24 24"><path d="M6.6 10.8a15 15 0 0 0 6.6 6.6l2.2-2.2c.3-.3.7-.4 1-.2 1.1.4 2.3.6 3.6.6.6 0 1 .4 1 1V20c0 .6-.4 1-1 1A17 17 0 0 1 3 4c0-.6.4-1 1-1h3.5c.6 0 1 .4 1 1 0 1.3.2 2.5.6 3.6.1.3 0 .7-.2 1z" fill="#fff"/></svg></span>
  <span>Call Now !! 08 5550 1427</span>
</div>
<div class="abs promo">
  <span class="ico-round"><svg width="16" height="16" viewBox="0 0 24 24"><path d="M12 2l3 6.6 7.2.8-5.4 4.9 1.5 7.1L12 17.8 5.7 21.4l1.5-7.1L1.8 9.4 9 8.6z" fill="#fff"/></svg></span>
  <span>5% Discount on order over $199</span>
</div>

<section class="abs hero" role="img" aria-label="Photo of smiling factory workers, one in a hard hat holding a clipboard"></section>
<div class="abs hero-kicker">Custom Sewn Goods Made to Your Specifications</div>
<h1 class="abs hero-title" style="font-weight:400">Asia Outsourcing made<br>easy way</h1>
<div class="abs hero-btn">read more</div>

<h2 class="abs sec-title" style="top:866px;font-weight:400">Sourcing <em>custom goods</em> in china</h2>
<div class="abs rule" style="left:307px;top:929px;width:570px"><i></i></div>
<p class="abs copy" style="left:150px;top:958px;width:900px">We outsource sewing services direct from China. Our long-established and extensive network of offshore factory-partners provides our clients with access to a wide variety of contract sewing expertise from Chinese manufacturers. Clients only need to communicate with our US agents, but will have the benefits of the cost savings &amp; quality workmanship from offshore outsourcing from Asia.</p>
<svg class="abs" style="left:566px;top:1088px" width="32" height="20" viewBox="0 0 32 20"><polyline points="3,4 16,16 29,4" fill="none" stroke="var(--green)" stroke-width="3"/></svg>

<!-- product categories -->
<article class="abs card" style="left:167px;top:1196px"><div class="card-head navy">Bags</div><div class="card-body"><div class="card-photo" role="img" aria-label="Photo of a messenger bag" style="background:linear-gradient(135deg,#5a5a5a,#2a2a2a 60%,#a32a2a)"></div><div class="card-label">lorem ipsum dolor</div></div></article>
<article class="abs card" style="left:467px;top:1196px"><div class="card-head navy">Covers</div><div class="card-body"><div class="card-photo" role="img" aria-label="Photo of a motorcycle cover" style="background:linear-gradient(135deg,#3a4cb0,#1c2a7a 60%,#c8c8c8)"></div><div class="card-label">lorem ipsum dolor</div></div></article>
<article class="abs card" style="left:763px;top:1196px"><div class="card-head navy">Gloves</div><div class="card-body"><div class="card-photo" role="img" aria-label="Photo of a pair of ski gloves" style="background:linear-gradient(135deg,#e6e6e6,#9a9a9a 60%,#333)"></div><div class="card-label">lorem ipsum dolor</div></div></article>

<div class="abs divider"></div>

<article class="abs card" style="left:167px;top:1556px"><div class="card-head green">Sporting Goods</div><div class="card-body"><div class="card-photo" role="img" aria-label="Photo of sports equipment bags" style="background:linear-gradient(135deg,#c23030,#3a3a3a 60%,#d8d8d8)"></div><div class="card-label">lorem ipsum dolor</div></div></article>
<article class="abs card" style="left:467px;top:1556px"><div class="card-head green">Cases</div><div class="card-body"><div class="card-photo" role="img" aria-label="Photo of colourful phone cases" style="background:linear-gradient(90deg,#2a2a2a,#4a3ab0,#a03ab0,#d03040,#e88020)"></div><div class="card-label">lorem ipsum dolor</div></div></article>
<article class="abs card" style="left:763px;top:1556px"><div class="card-head green">Sewn Goods</div><div class="card-body"><div class="card-photo" role="img" aria-label="Photo of fabric under a sewing machine needle" style="background:linear-gradient(135deg,#e8e0dc,#c23a3a 60%,#7a1a1a)"></div><div class="card-label">lorem ipsum dolor</div></div></article>

<h2 class="abs sec-title" style="top:1898px;color:var(--ink);font-weight:400">Don’t go it alone</h2>
<div class="abs rule" style="left:474px;top:1962px;width:306px"><i></i></div>
<p class="abs copy" style="left:148px;top:2001px;width:932px;line-height:24.6px">Brellin Trade Partners has been sourcing custom sewn goods in Asia since 1998. We work with our clients by matching their unique production needs with the best possible China sewing factories. We manage the entire process from start to finish, by first identifying the best factories to quote each job. The next step is negotiating the best (fair) price possible. We complete the process by monitoring the quality of the goods during production, and then managing the ocean logistics, customs clearances and local delivery right to your door. Our services and our total commitment to customer satisfaction help level the playing field by giving our customers&nbsp; to low cost, high quality China contract sewing.</p>

<footer class="abs footer"></footer>

<div class="abs f-head" style="left:100px;top:2282px">About us</div>
<div class="abs" style="left:100px;top:2314px;display:flex;flex-direction:column;gap:18px">
  <div class="f-row"><span class="f-ico"><svg width="18" height="18" viewBox="0 0 24 24"><path d="M6.6 10.8a15 15 0 0 0 6.6 6.6l2.2-2.2c.3-.3.7-.4 1-.2 1.1.4 2.3.6 3.6.6.6 0 1 .4 1 1V20c0 .6-.4 1-1 1A17 17 0 0 1 3 4c0-.6.4-1 1-1h3.5c.6 0 1 .4 1 1 0 1.3.2 2.5.6 3.6.1.3 0 .7-.2 1z" fill="#fff"/></svg></span><span>Our support hotline is available<br>24/5 a day: +1 555 014 2880,<br>+1 555 014 2881</span></div>
  <div class="f-row"><span class="f-ico"><svg width="18" height="18" viewBox="0 0 24 24"><circle cx="12" cy="13" r="8" fill="none" stroke="#fff" stroke-width="2"/><polyline points="12,9 12,13 15,15" fill="none" stroke="#fff" stroke-width="2"/></svg></span><span><b>Mo</b> – <b>Fr</b> 9.00 – 17.00<br><b>Sa</b> 9.00 – 15.00<br><b>Su</b> Closed</span></div>
  <div class="f-row" style="align-items:center"><span class="f-ico"><svg width="18" height="18" viewBox="0 0 24 24"><rect x="4" y="6" width="16" height="14" fill="none" stroke="#fff" stroke-width="2"/><line x1="12" y1="6" x2="12" y2="13" stroke="#fff" stroke-width="2"/><line x1="4" y1="10" x2="20" y2="10" stroke="#fff" stroke-width="2"/></svg></span><b>Delivery</b></div>
</div>

<div class="abs f-head" style="left:363px;top:2282px">Follow us</div>
<div class="abs fb" style="left:363px;top:2310px">
  <div class="fb-top"><span class="fb-mark"></span><span>harborthemes.example<br><span class="fb-follow"></span></span></div>
  <div class="fb-count">72 people follow harborthemes.example</div>
  <div class="fb-grid" role="img" aria-label="Grid of follower profile photos"><span></span><span></span><span></span><span></span><span></span><span></span><span></span><span></span></div>
  <div class="fb-foot">Social feed plugin</div>
</div>

<div class="abs f-head" style="left:626px;top:2282px">Product tags</div>
<div class="abs tags" style="left:626px;top:2306px"><span>ACCESSORIES</span><span>BIKINI</span><span>FISHING EQUIPMENT</span><span>LURE</span><span>REEL</span><span>ROD</span><span>SWIMGEAR</span><span>SWIMMING</span><span>SWIMWEAR</span></div>

<div class="abs f-head" style="left:889px;top:2282px">Our stores</div>
<div class="abs stores" style="left:889px;top:2306px">
  <div>London<b>›</b></div><div>Dubai<b>›</b></div><div>Berlin<b>›</b></div><div>New York<b>›</b></div><div>Moscow<b>›</b></div>
</div>

<div class="abs footbar">Copyright © 2015 Brellin Trade Partners, LLC. | USA - Hong Kong - Taipei</div>

</body>
</html>
```